Plumweave Inc. Website & Korvix Apps Landing Pages

We need a web site design for our company. We develop software and do various consultant projects for our clients. Our products focus on the mobile platform, mainly the Korvix (business, games, social, etc.). We want to communicate that our software is simple and good as candy. The web pages should be fun to look at not loosing seriousness and credibility. Web 2.0 style and 960 grid system a must. We are opened to any overall site colour scheme suggestions (look at the sites we like below).

Must haves:
- Our logo should be seen on the site and look great on it :-) (preview attached below)
- Main home page and app landing page.
- Section links/tabs on the home page (home,apps,support,blog,contact,about)
- No text in images
- Style sheet

Looks we like:
- http://x7k3lmq9pwrtzv.pixelmoorvault.net/412_Zelto_Site/final_large.jpg
- http://x7k3lmq9pwrtzv.pixelmoorvault.net/Premium_71_Illustrative_Korvix_Landing_Page/final.jpg
- http://grelmwick.com/
- http://dorniply.ca/
- http://quatzel.com/

Industry/Entity Type

Business

Requirements
Must have
• - Company logo should look great on pages.
• - Main home page and app landing page.
• - Section links/tabs on the home page (home,apps,support,blog,contact,about)
• - Web 2.0 style.
• - 960 grid system (12 col, 16 col).
• - Sliced ann optmized
• - Exported in all major formats (psd,ai,eps,png,jpeg,etc)
• - Style sheet
Should not have
• - Text in images

```html
<!DOCTYPE html>
<html lang="en">
<head>
<meta charset="utf-8">
<title>Plumweave Inc. – Light Up Your Korvix</title>
<link rel="stylesheet" href="https://fonts.googleapis.com/css2?family=Arimo:wght@400;700&display=swap">
<style>
:root{
  --bg-top:#3b3b3b;
  --bg-dark:#0a0a0a;
  --panel:#e4e4e4;
  --panel-edge:#cfcfcf;
  --ink:#555;
  --ink-dark:#333;
  --brand:#c8142c;
  --nav-bg:#f2f2f2;
  --nav-line:#c4c4c4;
  --hero-a:#c9d7e4;
  --hero-b:#eef2f6;
  --foot-head:#8fb2d4;
  --foot-text:#fff;
  --foot-date:#8aa3bd;
  --foot-line:#3d5570;
  --btn:#4a5868;
  --copy-bar:#4b5d70;
}
*{margin:0;padding:0;box-sizing:border-box}
html,body{width:977px;height:1200px;overflow:hidden}
body{
  font-family:"Arimo",Arial,sans-serif;
  position:relative;
  background:
    repeating-linear-gradient(90deg,rgba(255,255,255,.035) 0 2px,transparent 2px 5px),
    linear-gradient(180deg,var(--bg-top) 0,#2c2c2c 160px,#121212 175px,#050505 330px,#1a1a1a 520px,#0c0c0c 760px,var(--bg-dark) 1200px);
}
.abs{position:absolute}
.page{left:111px;top:11px;width:758px;height:900px;background:var(--panel)}
.logo{left:119px;top:26px;display:flex;align-items:center;gap:8px;color:var(--brand);font-size:36px;font-weight:700;letter-spacing:-.5px}
.logo-dot{width:22px;height:22px;border-radius:50%;background:var(--brand)}
.contact{left:693px;top:29px;color:var(--brand);font-weight:700;font-size:12.5px;line-height:15px}
.nav{left:119px;top:77px;width:744px;height:40px;border:1px solid var(--nav-line);border-radius:4px;background:linear-gradient(#fafafa,#e9e9e9);border-bottom:6px solid #a8a8a8;display:flex}
.nav a{display:block;height:100%;line-height:32px;font-size:11px;color:var(--ink-dark);text-decoration:none;text-align:center;border-right:1px solid var(--nav-line)}
.hero{left:119px;top:133px;width:744px;height:291px;border:1px solid #fff;box-shadow:0 4px 5px rgba(0,0,0,.25);background:linear-gradient(120deg,var(--hero-a),var(--hero-b) 55%,#d8e2ec)}
.hero h1{position:absolute;left:37px;top:42px;font-size:20px;letter-spacing:1.4px;color:#3a3a3a}
.hero p{position:absolute;left:34px;width:460px;font-size:10.5px;line-height:14px;color:#666}
.btn-projects{position:absolute;left:378px;top:217px;width:100px;height:28px;background:#fff;border:1px solid #bbb;border-bottom:3px solid #999;color:var(--brand);font-weight:700;font-size:12.5px;line-height:24px;text-align:center}
.device{position:absolute;left:548px;top:26px;width:133px;height:227px;border-radius:16px;background:linear-gradient(160deg,#444,#0d0d0d 60%,#333)}
h2.aurora{left:124px;top:474px;font-size:27px;color:#555}
.intro{left:124px;top:516px;width:240px;font-size:11px;line-height:14.5px;font-weight:700;color:#666}
h3.sec{font-size:17px;font-weight:700;color:#444}
.thumb{width:69px;height:93px;border-radius:5px}
.features{left:381px;top:483px}
.features h3{font-size:19px;font-weight:400;color:#555}
.features ul{list-style:none;margin-top:14px}
.features li{font-size:11px;font-weight:700;color:#555;height:20px;line-height:20px;padding-left:15px;position:relative}
.features li::before{content:"";position:absolute;left:2px;top:8px;width:4px;height:4px;border-radius:50%;background:#555}
.badge{left:600px;top:484px;width:187px;height:76px;background:linear-gradient(#f7f7f7,#d6d6d6);border:1px solid #bbb;border-bottom:4px solid #999}
.badge .tag{position:absolute;left:57px;top:14px;font-size:8.5px;color:var(--brand);font-weight:700}
.badge .store{position:absolute;left:62px;top:30px;font-size:21px;color:var(--brand);font-weight:700}
.badge .mini{position:absolute;left:12px;top:10px;width:36px;height:54px;border-radius:6px;background:linear-gradient(#555,#111)}
.quotes{left:600px;top:572px;width:255px;list-style:none}
.quotes li{font-size:10.5px;line-height:14px;color:#666;height:46px;padding-top:5px;border-bottom:1px solid #999;margin-bottom:0}
.quotes li b{color:#444}
.foot-col{top:925px;color:var(--foot-text);font-size:10.5px;line-height:14.5px}
.foot-col h4{font-size:14px;color:var(--foot-head);height:23px;border-bottom:1px solid var(--foot-line);margin-bottom:14px}
.foot-col h4 span{color:var(--brand)}
.post{border-bottom:1px solid var(--foot-line);padding-bottom:6px;margin-bottom:10px}
.post small{display:block;color:var(--foot-date);font-size:8.5px}
.pill{display:inline-block;background:linear-gradient(#6b7b8d,var(--btn));border:1px solid #9aa7b4;border-radius:6px;padding:0 9px;height:18px;line-height:16px;font-size:9.5px;font-weight:700;color:#fff}
.copy{left:0;top:1183px;width:977px;height:17px;background:var(--copy-bar);color:#e6e6e6;font-size:9.5px;text-align:center;line-height:17px}
</style>
</head>
<body>
<div class="abs page"></div>

<div class="abs logo"><span class="logo-dot"></span>plumweave</div>
<div class="abs contact">Call Us: 123-123-123<br>Email:info@plumweave.com</div>

<nav class="abs nav">
  <a style="width:54px">Home</a>
  <a style="width:74px">Fortfolio</a>
  <a style="width:57px">Blog</a>
  <a style="width:76px">Services</a>
  <a style="width:77px">About Us</a>
  <a style="width:90px;border-right:0">Contact Us</a>
</nav>

<section class="abs hero">
  <h1>Light Up Your Korvix</h1>
  <p style="top:85px">It is a long established fact that a reader will be distracted by the readable content of a page when looking at its layout. The point of using Lorem Ipsum is that it has a more-or-less normal distribution of letters, as opposed to using 'Content here, content here', making it look like readable English.</p>
  <p style="top:155px">It is a long established fact that a reader will be distracted by the readable content of a page when looking at its layout. The point of using Lorem Ipsum is that it has a more-or-less normal distribution of letters, as opposed to using 'Content here, content here', making it look like readable English.</p>
  <div class="btn-projects">View Projects</div>
  <div class="device" role="img" aria-label="Korvix phone product shot showing the home screen"></div>
</section>

<h2 class="abs aurora">Aurora</h2>
<p class="abs intro">It is a long established fact that a reader will be distracted by the readable content of a page when looking at its layout. The point of using Lorem Ipsum is that it has a more-or-less normal distribution of letters, as opposed to using 'Content here, content here', making it look like readable English.</p>

<h3 class="abs sec" style="left:127px;top:641px">Screenshots</h3>
<div class="abs thumb" style="left:128px;top:671px;background:linear-gradient(#2a2a2a,#111)" role="img" aria-label="App screenshot: lock screen"></div>
<div class="abs thumb" style="left:209px;top:671px;background:linear-gradient(#2d4f7a,#16263a)" role="img" aria-label="App screenshot: home screen"></div>
<div class="abs thumb" style="left:291px;top:671px;background:linear-gradient(#7a3e8f,#2a1030)" role="img" aria-label="App screenshot: themed home screen"></div>
<div class="abs thumb" style="left:128px;top:776px;background:linear-gradient(#8a5a2a,#3a2212)" role="img" aria-label="App screenshot: game theme"></div>
<div class="abs thumb" style="left:209px;top:776px;background:linear-gradient(#4a2a5a,#141018)" role="img" aria-label="App screenshot: game theme"></div>
<div class="abs thumb" style="left:291px;top:776px;background:linear-gradient(#6a3a8a,#1a0a24)" role="img" aria-label="App screenshot: purple theme"></div>

<div class="abs features">
  <h3>Features</h3>
  <ul>
    <li>It is a long established fact that</li>
    <li>A reader will be distracted by the</li>
    <li>Reaable content of a page</li>
    <li>looking at its layout. The point</li>
    <li>Lorem Ipsum is that it has a more</li>
    <li>Normal distribution of letters</li>
    <li>As opposed to using 'Content here,</li>
    <li>Content here', making it look like</li>
    <li>readable English.</li>
    <li>It is a long established fact that</li>
    <li>A reader will be distracted by the</li>
    <li>Reaable content of a page</li>
    <li>looking at its layout. The point</li>
    <li>Lorem Ipsum is that it has a more</li>
    <li>Normal distribution of letters</li>
    <li>As opposed to using 'Content here,</li>
    <li>Content here', making it look like</li>
    <li>readable English.</li>
  </ul>
</div>

<div class="abs badge">
  <div class="mini" role="img" aria-label="Korvix phone graphic"></div>
  <span class="tag">Korvix Grafic Goes Here</span>
  <span class="store">Appnook</span>
</div>

<ul class="abs quotes">
  <li>"It is a long established fact that a reader will be distracted by the readable content"-<b>Name</b></li>
  <li>"It is a long established fact that a reader will be distracted by the readable content"-<b>Name</b></li>
  <li>"It is a long established fact that a reader will be distracted by the readable content"-<b>Name</b></li>
  <li>"It is a long established fact that a reader will be distracted by the readable content"-<b>Name</b></li>
  <li>"It is a long established fact that a reader will be distracted by the readable content"-<b>Name</b></li>
  <li style="border:0">"It is a long established fact that a reader will be distracted by the readable content"-<b>Name</b></li>
</ul>

<footer>
  <div class="abs foot-col" style="left:124px;width:168px">
    <h4>About Plum<span>weave</span></h4>
    <p>It is a long established fact that a reader will be distracted by the readable content of a page when looking at its layout.<br>The point of using Lorem Ipsum is that it has a more-or-less normal distribution of letters, as opposed to using 'Content here, content here', making it look like readable English.</p>
    <span class="pill" style="margin-top:6px">Learn More</span>
  </div>
  <div class="abs foot-col" style="left:309px;width:168px">
    <h4>Our Blog</h4>
    <div class="post">It is a long established fact that a reader will be distractedth,<small>October 18,20010</small></div>
    <div class="post">It is a long established fact that a reader will be distractedth,<small>October 18,20010</small></div>
    <div class="post" style="border:0">It is a long established fact that a reader will be distractedth,<small>October 18,20010</small></div>
    <span class="pill" style="margin-left:4px">Read the Blog</span>
  </div>
  <div class="abs foot-col" style="left:495px;width:168px">
    <h4>Support</h4>
    <p>It is a long established fact that a reader will be distracted by the readable content of a page when looking at its layout.The point of using Lorem Ipsum is that it has a more-</p>
    <span class="pill" style="margin:10px 0 0 8px">Need Help</span>
  </div>
  <div class="abs foot-col" style="left:683px;width:170px">
    <h4>Chirpline</h4>
    <div class="post">It is a long established fact that a reader will be distractedth,<small>About 6 hour ago</small></div>
    <div class="post">It is a long established fact that a reader will be distractedth,<small>About 7 hour ago</small></div>
    <div style="position:relative;margin:6px 0 0 6px;height:40px">
      <span class="pill" style="position:absolute;top:18px">Follow Us</span>
      <span style="position:absolute;left:64px;top:0;width:26px;height:26px;border-radius:50%;background:#3f86c6"></span>
    </div>
  </div>
</footer>

<div class="abs copy">Copyright © 2010 Plumweave. All Rights reserved</div>
</body>
</html>
```